New Logo and Business Card

Want new logo and business card for multi brand website. Attached are the logos for the back of the card.
We want a new logo for the front, the name "Tallvisto" as the company name.
The logo can just be an "O" and a "B" for simplicity. With the text "Tallvisto" after it.
For the business card use this info:
Dale Furnow, PEng MBA
President
dale.furnow@tallvisto.ca
+14035512839
Industry/Entity Type
Business
Logo Text
Tallvisto
Logo styles of interest
Lettermark Logo

```html
<!DOCTYPE html>
<html lang="en">
<head>
<meta charset="utf-8">
<title>Tallvisto – Business Card</title>
<link rel="stylesheet" href="https://fonts.googleapis.com/css2?family=Noto+Serif:wght@400;700&display=swap">
<style>
  :root {
    --teal: #336968;
    --ink: #000000;
    --wave-grey: #a9a9a9;
    --paper: #ffffff;
    --mark-faint: rgba(255, 255, 255, 0.28);
    --mark-grey: #8a8a8a;
  }
  * { margin: 0; padding: 0; box-sizing: border-box; }
  html, body {
    width: 1200px;
    height: 686px;
    overflow: hidden;
    background: var(--paper);
  }
  .canvas {
    position: relative;
    width: 1200px;
    height: 686px;
    background: var(--paper);
    font-family: "Noto Serif", Georgia, serif;
  }

  /* Business card front */
  .card {
    position: absolute;
    left: 91px;
    top: 80px;
    width: 664px;
    height: 378px;
    background: var(--teal);
    overflow: hidden;
  }
  .card-wave {
    position: absolute;
    inset: 0;
    width: 100%;
    height: 100%;
  }
  .card-mark-faint {
    position: absolute;
    left: 240px;
    top: 110px;
    width: 150px;
    height: 150px;
    border: 6px solid var(--mark-faint);
  }
  .card-brand {
    position: absolute;
    left: 62px;
    top: 38px;
    display: flex;
    align-items: center;
    gap: 26px;
  }
  .brand-square {
    width: 62px;
    height: 62px;
    border: 4px solid var(--paper);
    flex: none;
  }
  .brand-name {
    color: var(--paper);
    font-weight: 700;
    text-transform: uppercase;
    letter-spacing: 3px;
    line-height: 1;
  }
  .card-brand .brand-name { font-size: 44px; }

  .card-holder {
    position: absolute;
    right: 42px;
    top: 160px;
    text-align: right;
    color: var(--paper);
    font-size: 22px;
    line-height: 1.2;
  }
  .card-contact {
    position: absolute;
    left: 41px;
    top: 306px;
    color: var(--paper);
    font-size: 18px;
    line-height: 1.3;
  }
  .card-mark-small {
    position: absolute;
    right: 42px;
    bottom: 24px;
    width: 40px;
    height: 40px;
    border: 3px solid var(--mark-grey);
  }

  /* Brand banner */
  .banner {
    position: absolute;
    left: 0;
    top: 526px;
    width: 1200px;
    height: 160px;
    background: var(--teal);
  }
  .banner-brand {
    position: absolute;
    left: 66px;
    top: 50%;
    transform: translateY(-50%);
    display: flex;
    align-items: center;
    gap: 34px;
  }
  .banner-brand .brand-square { width: 76px; height: 76px; border-width: 5px; }
  .banner-brand .brand-name { font-size: 46px; }
  .banner-mark-faint {
    position: absolute;
    left: 968px;
    top: 34px;
    width: 92px;
    height: 92px;
    border: 5px solid var(--mark-faint);
  }
</style>
</head>
<body>
  <main class="canvas">
    <section class="card" aria-label="Business card front">
      <svg class="card-wave" viewBox="0 0 664 378" preserveAspectRatio="none" aria-hidden="true">
        <path d="M0,258 C80,212 200,214 330,248 S560,290 664,286 L664,378 L0,378 Z" fill="var(--wave-grey)"/>
        <path d="M0,292 C100,248 220,252 340,268 S560,292 664,290 L664,378 L0,378 Z" fill="var(--ink)"/>
      </svg>
      <div class="card-mark-faint" aria-hidden="true"></div>

      <div class="card-brand">
        <span class="brand-square" aria-hidden="true"></span>
        <span class="brand-name">Tallvisto</span>
      </div>

      <div class="card-holder">
        <p class="holder-name">Dale Furnow, PEng MBA</p>
        <p class="holder-title">President</p>
      </div>

      <div class="card-contact">
        <p class="contact-email">dale.furnow @ tallvisto.ca</p>
        <p class="contact-phone">+14035512839</p>
      </div>
      <div class="card-mark-small" aria-hidden="true"></div>
    </section>

    <section class="banner" aria-label="Brand banner">
      <div class="banner-brand">
        <span class="brand-square" aria-hidden="true"></span>
        <span class="brand-name">Tallvisto</span>
      </div>
      <div class="banner-mark-faint" aria-hidden="true"></div>
    </section>
  </main>
</body>
</html>
```